Tarvo Gym Direct Mail for Weight Loss Challenge

We need a two-sided direct mail piece made for all three of our fitness facilities that promotes a weight loss challenge. The weight loss challenge (Kick Up Your Game! (our gym is eco-friendly and our logo is a leaf, hence the sprout)) is simple- lose 1 lb, get $20 (up to $200). The challenge is 8 weeks long and they must join before March 31st to be eligible. Attached is our logo, and other direct mail pieces that have been created in the past. We like cleaner looking pieces that do not look busy, but rather clean and effective, with only a few messages. On the front, we'd like this weight loss challenge, and then on the back left, a description of our two membership options- 1. Tally Plan- the more you workout, the less you pay. As Low As $0/month. (the more times you come in, the less your dues are) and 2. Month to Month- $19/month, month to month, with zero long-term contracts. In the middle, the locations as you can see on the other pieces, and then on the right, space for postage like we already have. We would need three pieces created, since these will be going out to three separate locations. The only difference will be the location of, for example, Westfallow highlighted more than the other two locations, and so on.

```html
<!DOCTYPE html>
<html lang="en">
<head>
<meta charset="utf-8">
<title>Tarvo Gym – Weight Loss Challenge Mailer</title>
<link rel="stylesheet" href="https://fonts.googleapis.com/css2?family=Oswald:wght@500;700&family=Roboto:wght@400;700;900&display=swap">
<style>
  :root {
    --bg: #e8e8e8;
    --paper: #ffffff;
    --green: #5e9b35;
    --green-bright: #74b043;
    --green-panel: #8cc063;
    --green-dark: #5f8f3e;
    --grey-band: #dcdcdc;
    --grey-text: #7d7d7d;
    --ink: #1f2a1a;
    --line: #7a7a7a;
  }
  * { margin: 0; padding: 0; box-sizing: border-box; }
  html, body { width: 1200px; height: 720px; overflow: hidden; }
  body { background: var(--bg); position: relative; font-family: "Roboto", Arial, sans-serif; }

  .card { position: absolute; top: 203px; width: 536px; height: 292px; background: var(--paper); overflow: hidden; }
  .card--front { left: 44px; }
  .card--back { left: 627px; }

  /* ---------- Front ---------- */
  .front-side { position: absolute; left: 0; top: 0; width: 192px; height: 292px; }
  .brand { position: absolute; left: 0; top: 12px; width: 192px; display: flex; flex-direction: column; align-items: center; gap: 8px; }
  .brand__dot { width: 22px; height: 22px; border-radius: 50%; background: var(--green-bright); }
  .brand__name { font-weight: 400; font-size: 15px; letter-spacing: 3px; color: var(--green); }
  .headline-panel { position: absolute; left: 0; top: 74px; width: 192px; height: 180px; background: var(--grey-band); }
  .headline { position: absolute; left: 0; top: 82px; width: 192px; text-align: center; font-family: "Oswald", "Arial Narrow", sans-serif; font-weight: 700; color: var(--green); line-height: 1; text-transform: uppercase; }
  .headline__big { display: block; font-size: 44px; }
  .headline__small { display: block; font-size: 19px; margin: 2px 0 4px; }
  .deadline { position: absolute; left: 0; width: 192px; text-align: center; top: 260px; font-size: 6px; font-weight: 700; color: #333; letter-spacing: 0.2px; text-transform: uppercase; }

  .photo { position: absolute; left: 192px; top: 0; width: 344px; height: 292px;
    background: linear-gradient(180deg, rgba(255,255,255,0) 70%, #fff 100%),
                linear-gradient(110deg, #c9b3a5 0%, #7f8fa0 35%, #3f5670 60%, #aab8c4 85%, #d9dde2 100%); }
  .challenge-band { position: absolute; left: 192px; top: 0; width: 344px; height: 69px; background: rgba(210,210,210,0.85); }
  .challenge-band__title { position: absolute; left: 0; width: 100%; top: 24px; text-align: center; font-weight: 900; font-size: 15px; color: #fff; letter-spacing: 0.8px; text-transform: uppercase; }
  .offer { position: absolute; left: 215px; top: 165px; font-weight: 900; color: #fff; font-size: 28px; line-height: 1.1; text-transform: uppercase; }
  .offer__note { font-size: 17px; }

  /* ---------- Back ---------- */
  .plans { position: absolute; left: 0; top: 0; width: 135px; height: 292px; text-align: center; font-family: "Oswald", "Arial Narrow", sans-serif; font-weight: 700; color: var(--green); text-transform: uppercase; line-height: 1; }
  .plans__title { margin-top: 6px; font-size: 25px; }
  .plans__small { font-size: 8px; margin-top: 4px; }
  .plans__price { font-size: 22px; margin-top: 2px; }
  .plans__per { font-size: 11px; margin-top: 1px; }
  .plans__tagline { margin-top: 9px; background: var(--grey-band); padding: 6px 0; font-size: 7.5px; color: var(--grey-text); line-height: 1.2; }
  .plans__tagline b { font-size: 9.5px; display: block; }
  .plans__title--alt { font-size: 16px; margin-top: 8px; }
  .plans__title--alt em { font-style: normal; font-size: 9px; }
  .contracts { display: flex; justify-content: center; align-items: center; gap: 4px; margin-top: 6px; font-family: "Roboto", Arial, sans-serif; color: #222; }
  .contracts__zero { font-size: 16px; font-weight: 900; }
  .contracts__text { font-size: 6px; font-weight: 900; text-align: left; line-height: 1.1; }

  .locations { position: absolute; left: 135px; top: 0; width: 135px; height: 252px; background: var(--green-panel); }
  .locations__cap { position: absolute; left: 0; top: 0; }
  .locations__brand { position: absolute; left: 0; top: 10px; width: 135px; display: flex; flex-direction: column; align-items: center; gap: 4px; }
  .locations__brand .brand__dot { width: 16px; height: 16px; }
  .locations__brand .brand__name { font-size: 10px; letter-spacing: 2px; }
  .location { position: absolute; left: 0; width: 135px; text-align: center; color: var(--ink); }
  .location__name { font-weight: 700; font-size: 11px; text-transform: uppercase; margin-bottom: 2px; }
  .location__addr { font-size: 7.5px; line-height: 1.35; }

  .stamp { position: absolute; left: 452px; top: 29px; width: 59px; height: 55px; border: 1.5px dashed #444; }
  .address-line { position: absolute; left: 300px; width: 202px; height: 1px; background: var(--line); }
</style>
</head>
<body>

  <section class="card card--front" aria-label="Mailer front">
    <div class="front-side">
      <div class="brand">
        <span class="brand__dot"></span>
        <span class="brand__name">TARVO GYM</span>
      </div>
      <div class="headline-panel"></div>
      <h1 class="headline">
        <span class="headline__big">Kick Up</span>
        <span class="headline__small">Your Game!</span>
        <span class="headline__big">8 Week</span>
        <span class="headline__small">Challenge</span>
      </h1>
      <p class="deadline">Must join before March 31st to be eligible</p>
    </div>
    <div class="photo" role="img" aria-label="Photo of a person lifting a chrome dumbbell"></div>
    <div class="challenge-band"><h2 class="challenge-band__title">The Weight Loss Challenge</h2></div>
    <p class="offer">Lose 1 lb<br>Get $20 <span class="offer__note">(Up to $200)</span></p>
  </section>

  <section class="card card--back" aria-label="Mailer back">
    <div class="plans">
      <h2 class="plans__title">Tally Plan</h2>
      <p class="plans__small">As low as</p>
      <p class="plans__price">$0</p>
      <p class="plans__per">Per month</p>
      <p class="plans__tagline">The more you work out<b>the less you pay</b></p>
      <h2 class="plans__title--alt">Month <em>to</em> Month</h2>
      <p class="plans__price">$19</p>
      <p class="plans__per">Per month</p>
      <div class="contracts"><span class="contracts__zero">0</span><span class="contracts__text">LONG TERM<br>CONTRACTS</span></div>
    </div>

    <div class="locations">
      <svg class="locations__cap" width="135" height="82" viewBox="0 0 135 82">
        <polygon points="0,0 135,0 135,60 67.5,82 0,60" fill="var(--green-dark)"/>
        <polygon points="0,0 135,0 135,48 67.5,70 0,48" fill="#fff"/>
      </svg>
      <div class="locations__brand">
        <span class="brand__dot"></span>
        <span class="brand__name">TARVO GYM</span>
      </div>
      <div class="location" style="top:87px">
        <p class="location__name">Brookhaven</p>
        <p class="location__addr">480 Birchwood Ave.<br>Brookhaven, ST 00101</p>
      </div>
      <div class="location" style="top:133px">
        <p class="location__name">Ridgemoor</p>
        <p class="location__addr">1930 Alder Ln.<br>Ridgemoor, ST 00202</p>
      </div>
      <div class="location" style="top:180px">
        <p class="location__name">Westfallow</p>
        <p class="location__addr">Maple Commons<br>Plaza, Suite 204<br>7320 S. Orchard Rd.<br>Westfallow, ST 00303</p>
      </div>
    </div>

    <div class="stamp"></div>
    <div class="address-line" style="top:134px"></div>
    <div class="address-line" style="top:166px"></div>
    <div class="address-line" style="top:198px"></div>
    <div class="address-line" style="top:231px"></div>
  </section>

</body>
</html>
```